Post Lockdown Ortho Special

We are running a special for (Ortho) Braces/Clear Aligner (Quorvelina), till July 31st 2020. Up to $2,000 off with free Consultation and Xrays.

We need a ad to run in different formats.

Maybe something with: what better time to get braces when you have to wear a mask all the time.

Trying to rebuild our business and get people in for free consultations.

```html
<!DOCTYPE html>
<html lang="en">
<head>
<meta charset="utf-8">
<title>Post Lockdown Ortho Special – Pinecrest Family Dentistry</title>
<link href="https://fonts.googleapis.com/css2?family=Bebas+Neue&family=Montserrat:wght@400;600;700;800&display=swap" rel="stylesheet">
<style>
  :root {
    --cream: #fbf1ea;
    --cream-deep: #f4e2d7;
    --lavender: #7d62a8;
    --lavender-light: #a890cf;
    --plum: #33234f;
    --plum-mid: #5a4483;
    --ink: #232323;
    --skin-light: #f6ddd2;
    --skin-deep: #e9bfae;
    --gold: #e8c9a6;
    --white: #ffffff;
  }
  * { margin: 0; padding: 0; box-sizing: border-box; }
  html, body { width: 938px; height: 1200px; overflow: hidden; background: #ffffff; }
  .flyer {
    position: relative;
    width: 938px;
    height: 1200px;
    overflow: hidden;
    background: radial-gradient(ellipse at 30% 45%, #fff8f3 0%, var(--cream) 55%, var(--cream-deep) 100%);
    font-family: "Montserrat", sans-serif;
  }
  .portrait { position: absolute; inset: 0; }
  .brand {
    position: absolute; left: 48px; top: 92px;
    display: flex; align-items: center; gap: 16px;
  }
  .brand-dot { width: 62px; height: 62px; border-radius: 50%; background: var(--lavender); }
  .brand-name {
    font-weight: 700; color: var(--lavender); font-size: 22px; line-height: 1.15;
    letter-spacing: 0.5px;
  }
  .brand-doctor {
    margin-top: 6px; font-size: 11px; letter-spacing: 2px; text-transform: uppercase;
    color: var(--lavender); font-weight: 400;
  }
  .intro {
    position: absolute; left: 52px; top: 246px;
    color: var(--lavender); font-size: 35px; line-height: 1.3; font-weight: 400;
  }
  .intro strong { font-weight: 600; }
  .treatment {
    position: absolute; left: 50px; top: 420px;
    font-family: "Bebas Neue", sans-serif; font-size: 92px; line-height: 0.88;
  }
  .treatment .dark { color: var(--ink); }
  .treatment .accent { color: var(--lavender); }
  .deadline {
    position: absolute; left: 0; top: 806px; width: 456px; height: 48px;
    background: var(--plum); border-radius: 0 24px 24px 0;
    display: flex; align-items: center; padding-left: 44px;
    font-size: 28px; color: var(--lavender-light); font-weight: 400; letter-spacing: 0.5px;
  }
  .deadline strong { color: var(--white); font-weight: 700; margin: 0 10px; }
  .waves { position: absolute; left: 0; top: 0; }
  .offer-badge {
    position: absolute; left: 52px; top: 890px; width: 264px; height: 264px;
    border-radius: 50%;
    background: linear-gradient(145deg, #ffffff, #b9b9bf 45%, #f4f4f6 70%, #9a9aa2);
    box-shadow: 0 6px 16px rgba(40,20,70,0.35);
  }
  .offer-core {
    position: absolute; inset: 14px; border-radius: 50%;
    background: radial-gradient(circle at 50% 30%, var(--plum-mid), var(--plum) 75%);
    display: flex; flex-direction: column; align-items: center; justify-content: center;
    font-family: "Bebas Neue", sans-serif; color: var(--white); line-height: 0.9;
  }
  .offer-core .small { font-size: 48px; }
  .offer-core .amount { font-size: 82px; }
  .perks {
    position: absolute; left: 320px; top: 952px; width: 320px;
    border-top: 1.5px solid #8a8a8a; border-bottom: 1.5px solid #8a8a8a;
    padding: 14px 0 14px 36px;
    font-weight: 800; color: var(--plum); font-size: 25px; line-height: 1.25;
  }
  .contact {
    position: absolute; left: 0; width: 938px; top: 1127px;
    text-align: center; color: var(--white); font-size: 17px; line-height: 1.55;
  }
  .contact strong { color: var(--gold); font-weight: 600; }
  .contact .sep { margin: 0 8px; }
</style>
</head>
<body>
<main class="flyer">
  <svg class="portrait" width="938" height="1200" viewBox="0 0 938 1200" role="img" aria-label="Photo of a smiling young woman wearing clear braces, shown in close-up on the right side">
    <defs>
      <linearGradient id="skin" x1="0" y1="0" x2="1" y2="1">
        <stop offset="0" stop-color="var(--skin-light)"/>
        <stop offset="1" stop-color="var(--skin-deep)"/>
      </linearGradient>
    </defs>
    <path d="M470 0 H938 V1060 C860 1040 760 990 690 930 C620 860 570 760 560 660 C555 560 520 480 505 400 C490 300 465 200 470 0 Z" fill="url(#skin)"/>
  </svg>

  <svg class="waves" width="938" height="1200" viewBox="0 0 938 1200" aria-hidden="true">
    <path d="M0 905 C150 1000 300 1060 470 1075 C640 1090 800 1050 938 1010 V1200 H0 Z" fill="var(--lavender)"/>
    <path d="M0 930 C150 1030 300 1080 470 1092 C640 1100 800 1070 938 1035 V1200 H0 Z" fill="var(--white)"/>
    <path d="M0 950 C150 1050 300 1095 470 1103 C640 1110 800 1085 938 1055 V1200 H0 Z" fill="var(--plum)"/>
  </svg>

  <header class="brand">
    <span class="brand-dot"></span>
    <div>
      <div class="brand-name">Pinecrest<br>Family Dentistry</div>
      <div class="brand-doctor">Dr Maren Ashby</div>
    </div>
  </header>

  <p class="intro">We Are Running<br>a <strong>Special For</strong></p>

  <h1 class="treatment">
    <span class="dark">(Ortho)</span><br>
    <span class="accent">Braces/Clear<br>Aligner</span><br>
    <span class="dark">(Quorvelina)</span>
  </h1>

  <div class="deadline">TILL <strong>JULY 31ST</strong> 2020</div>

  <div class="offer-badge">
    <div class="offer-core">
      <span class="small">Up To</span>
      <span class="amount">$2,000</span>
      <span class="small">Off</span>
    </div>
  </div>

  <p class="perks">WITH FREE<br>CONSULTATION<br>AND X-RAYS</p>

  <footer class="contact">
    For More Information, Call Us : <strong>0198 765 432</strong> or<br>
    Mail us : <strong>hello@pinecrestsmiles.com</strong><span class="sep">|</span>Visit us: <strong>www.pinecrestsmiles.com</strong>
  </footer>
</main>
</body>
</html>
```